Digital Album Cover - Piano music for wedding ceremonies and receptions

I need cover art for a piano album project that will be distributed to TuneVault, Wavelane etc. Covert art required for front of album. At this stage physical CDs will not be printed nor required it is just a digital release.
Artist name: Toby Hargrove
Album Title: Gentle Keys Melodies Wedding Ceremonies and Receptions
Volume 3
Sample piano songs are on my tunecast page
https://tunecast.example/tobyhargrovekeys/sets/gentle-keys-melodies-vol-3
Previous album artwork used from sketch hive competitions winners
https://musicvault.example/au/artist/toby-hargrove/4830917265
Target Market(s)
brides to be
grooms to be
people interested in weddings
people enjoy love songs or easy listening music
Industry/Entity Type
Wedding
Look and feel
Each slider illustrates characteristics of the customer's brand and the style your logo design should communicate.

```html
<!DOCTYPE html>
<html lang="en">
<head>
<meta charset="utf-8">
<title>Toby Hargrove – Gentle Keys Melodies, Volume 3</title>
<link rel="stylesheet" href="https://fonts.googleapis.com/css2?family=Great+Vibes&family=Quicksand:wght@500&family=Lora:ital@1&display=swap">
<style>
  :root {
    --ink-deep: #121826;
    --ink-navy: #1a2233;
    --piano-black: #0e0f14;
    --bokeh-warm: #8a6a3e;
    --bokeh-light: #e8dcc0;
    --skin-warm: #c99a82;
    --skin-light: #e6c3ae;
    --key-ivory: #ece7de;
    --key-shadow: #a9a49c;
    --gold: #f1c76c;
    --white: #ffffff;
    --volume-grey: #3f3f3f;
  }
  * { margin: 0; padding: 0; box-sizing: border-box; }
  html, body {
    width: 1200px;
    height: 1200px;
    overflow: hidden;
    background: var(--ink-deep);
  }
  .album-cover {
    position: relative;
    width: 1200px;
    height: 1200px;
    overflow: hidden;
  }
  .cover-photo {
    position: absolute;
    inset: 0;
    background:
      /* warm bokeh glow, upper left */
      radial-gradient(ellipse 520px 260px at 480px 150px, rgba(232,220,192,0.55), transparent 70%),
      radial-gradient(ellipse 420px 300px at 120px 120px, rgba(138,106,62,0.75), transparent 75%),
      /* hands across the keys */
      radial-gradient(ellipse 520px 110px at 360px 440px, rgba(201,154,130,0.85), transparent 72%),
      radial-gradient(ellipse 560px 120px at 420px 610px, rgba(230,195,174,0.85), transparent 72%),
      /* ivory keyboard running diagonally to lower right */
      linear-gradient(122deg, transparent 0%, transparent 55%, rgba(169,164,156,0.9) 63%, var(--key-ivory) 72%, var(--key-ivory) 100%),
      /* dark piano body and upper right */
      linear-gradient(180deg, #2a2a30 0%, var(--piano-black) 35%, var(--ink-navy) 70%, var(--ink-deep) 100%);
  }
  .artist-name {
    position: absolute;
    left: 128px;
    top: 835px;
    font-family: "Great Vibes", cursive;
    font-size: 86px;
    line-height: 1.2;
    color: var(--gold);
    font-weight: 400;
    white-space: nowrap;
  }
  .album-title {
    position: absolute;
    left: 70px;
    top: 1012px;
    font-family: "Quicksand", sans-serif;
    font-weight: 500;
    font-size: 56px;
    line-height: 1;
    color: var(--white);
    white-space: nowrap;
  }
  .album-subtitle {
    position: absolute;
    left: 144px;
    top: 1082px;
    font-family: "Lora", serif;
    font-style: italic;
    font-size: 26px;
    color: var(--white);
    white-space: nowrap;
  }
  .volume-label {
    position: absolute;
    right: 48px;
    top: 1100px;
    font-family: "Lora", serif;
    font-style: italic;
    font-size: 36px;
    color: var(--volume-grey);
    white-space: nowrap;
  }
</style>
</head>
<body>
  <main class="album-cover">
    <div class="cover-photo" role="img" aria-label="Photograph of two hands playing an upright piano keyboard, with warm golden bokeh lights glowing in the background"></div>
    <h1 class="artist-name">Toby Hargrove</h1>
    <h2 class="album-title">Gentle Keys Melodies</h2>
    <p class="album-subtitle">Wedding Ceremonies and Receptions</p>
    <p class="volume-label">Volume 3</p>
  </main>
</body>
</html>
```